Move the hackers to Wordpress

Yep, we want to move https://www.tallowmarsh.com/ to Wordpress. It'll make it easier to update and add content. I'd like mostly the same look, but I'm not stuck with it.
Updates

DO NOT RESPOND OUTSIDE OF PIXEL HARBOR OR CONTACT US DIRECTLY.

Industry/Entity Type

Computer Security

Coding

Coded - Design and coding required

Font styles to use
Sans Serif

Colors
ec1f27

Requirements
Must have
• What I do want is:
• 1. Similar look to the existing site
• 2. Needs to work on one of the Wordpress hosting sites. I do NOT want to run my own Wordpress server.
• 3. Keep the animation in the top panel.
• 4. Mobile support
• The rest can be changed as needed.
Nice to have
• I like the transitions when the "services" panel shows up. Not stuck on it, but it is a nice touch.

```html
<!DOCTYPE html>
<html lang="en">
<head>
<meta charset="utf-8">
<title>Tallow Marsh — Information Security</title>
<link href="https://fonts.googleapis.com/css2?family=Open+Sans:wght@400;600;700;800&display=swap" rel="stylesheet">
<style>
:root{
  --red:#e02a21;
  --red-soft:#ec1f27;
  --hero-dark:#2c2c2e;
  --ink:#333;
  --muted:#666;
  --white:#fff;
  --footer:#222;
  --footer-base:#171717;
  --link-blue:#2ea3f2;
}
*{margin:0;padding:0;box-sizing:border-box}
html,body{width:1200px;height:3321px;overflow:hidden;background:var(--white)}
body{font-family:"Open Sans",Arial,sans-serif;color:var(--ink);position:relative}
.abs{position:absolute}

/* Hero */
.hero{top:0;left:0;width:1200px;height:587px;background:radial-gradient(ellipse at 70% 30%,#3a3a3c 0%,var(--hero-dark) 60%,#262628 100%)}
.hero-network{top:0;left:0;width:1200px;height:587px;background:linear-gradient(160deg,rgba(224,42,33,.06),rgba(255,255,255,.03) 50%,rgba(224,42,33,.05))}
.brand{left:110px;top:22px;display:flex;align-items:center;gap:10px}
.brand-square{width:28px;height:28px;background:var(--red)}
.brand-name{font-weight:800;font-size:26px;color:var(--red);letter-spacing:2px;text-transform:uppercase}
.main-nav{top:34px;left:500px;display:flex;gap:22px;font-size:14px;font-weight:600;color:var(--white);text-transform:uppercase}
.main-nav .current{color:var(--red)}
.search-icon{left:1066px;top:33px}
.hero-title{left:33px;top:318px;font-size:72px;font-weight:800;line-height:70px;color:var(--white)}

/* What we do */
.what-title{left:106px;top:658px;font-size:28px;font-weight:400;color:#222}
.what-lead{left:106px;top:693px;font-size:18px;color:#2a2a4a}
.what-body{left:106px;top:722px;width:640px;font-size:13.5px;line-height:22px;color:var(--muted)}
.what-mark{left:793px;top:660px;width:150px;display:flex;flex-direction:column;align-items:center;gap:12px}
.what-mark-square{width:150px;height:150px;background:var(--red)}
.what-mark-name{font-size:20px;font-weight:800;color:var(--red);text-transform:uppercase;letter-spacing:1px}
.wave{left:0;top:870px}

/* Services */
.services{left:0;top:952px;width:1200px;height:720px;background:var(--red)}
.services-title{left:106px;top:1030px;font-size:27px;color:var(--white)}
.service{width:290px;color:var(--white)}
.service h3{font-size:17px;font-weight:400;line-height:20px;margin-bottom:4px}
.service p{font-size:13.5px;line-height:22px}

/* About */
.about-title{left:0;width:1200px;top:1740px;text-align:center;font-size:28px;color:#222}
.about-sub{left:0;width:1200px;top:1780px;text-align:center;font-size:13.5px;color:var(--muted)}
.video{left:310px;top:1827px;width:565px;height:316px;background:linear-gradient(135deg,#1d2228,#3b4550 50%,#151a1f)}
.video-controls{left:310px;top:2110px;width:565px;height:33px;background:rgba(0,0,0,.75)}
.play-btn{left:568px;top:1960px;width:48px;height:48px;border-radius:50%;background:rgba(0,0,0,.6)}
.progress{left:358px;top:2125px;width:378px;height:4px;background:#555}
.time{left:744px;top:2118px;font-size:11px;color:#ccc}

/* Testimonial */
.testimonial{left:0;top:2214px;width:1200px;height:598px;background:var(--red)}
.quote-mark{top:2250px;font-size:260px;font-weight:800;line-height:260px;color:rgba(255,255,255,.35);font-family:Georgia,serif}
.avatar-frame{left:491px;top:2329px;width:204px;height:202px;background:var(--white)}
.avatar{left:507px;top:2345px;width:172px;height:172px;border-radius:50%;background:linear-gradient(#7dbb7a,#5b9e5b)}
.client-name{left:0;width:1200px;top:2592px;text-align:center;font-size:24px;color:var(--white)}
.client-quote{left:0;width:1200px;top:2630px;text-align:center;font-size:13.5px;line-height:23px;color:var(--white)}

/* Footer */
.footer{left:0;top:2812px;width:1200px;height:332px;background:var(--footer)}
.footer-heading{font-size:16px;color:var(--link-blue)}
.footer-brand{left:106px;top:2906px;display:flex;align-items:center;gap:8px}
.footer-brand .brand-square{width:20px;height:20px}
.footer-brand .brand-name{font-size:18px}
.quick-links{left:790px;top:2906px;list-style:none;font-size:13px;color:var(--white);line-height:27.7px}
.quick-links li::before{content:"";display:inline-block;width:4px;height:4px;border-radius:50%;background:var(--link-blue);margin-right:8px;vertical-align:middle}
.footer-base{left:0;top:3144px;width:1200px;height:44px;background:var(--footer-base)}
.social{left:920px;top:3157px;display:flex;gap:22px}
.social span{width:18px;height:18px;border-radius:50%;background:#666}
</style>
</head>
<body>

<section class="abs hero"></section>
<div class="abs hero-network" role="img" aria-label="Animated network of connected nodes and lines with red points"></div>
<div class="abs brand"><span class="brand-square"></span><span class="brand-name">Tallow Marsh</span></div>
<nav class="abs main-nav">
  <span class="current">Home</span><span>What We Do</span><span>Services</span><span>About</span><span>Press</span><span>Blog</span><span>Contact</span>
</nav>
<svg class="abs search-icon" width="16" height="16" viewBox="0 0 16 16"><circle cx="9.5" cy="6.5" r="5" fill="none" stroke="#fff" stroke-width="1.8"/><line x1="6" y1="10" x2="1.5" y2="14.5" stroke="#fff" stroke-width="1.8"/></svg>
<h1 class="abs hero-title">Offensive Services<br>From Offensive Minds</h1>

<h2 class="abs what-title">WHAT WE DO</h2>
<p class="abs what-lead">We are an information security company focusing on real world threats.</p>
<p class="abs what-body">Tallow Marsh is an information security consulting company that concentrates on the latest threats to organizations today. We perform in-depth analysis, determine organization/business risk, and find the vulnerabilities before the bad guys do. Our team includes internationally renowned experts who have been featured in international news outlets and conferences, including The Harbor Ledger, The Capital Courier, a Eastline News Documentary.</p>
<div class="abs what-mark"><span class="what-mark-square"></span><span class="what-mark-name">Tallow Marsh</span></div>

<svg class="abs wave" width="1200" height="90" viewBox="0 0 1200 90" preserveAspectRatio="none">
  <path d="M0 5 C300 70 700 80 1000 72 C1100 68 1160 40 1200 20 L1200 90 L0 90 Z" fill="#ef8a85"/>
  <path d="M0 30 C300 80 700 88 1000 82 C1100 80 1160 50 1200 28 L1200 90 L0 90 Z" fill="#fff"/>
  <path d="M0 40 C300 90 700 92 1000 86 C1100 84 1160 60 1200 38 L1200 90 L0 90 Z" fill="#e02a21"/>
</svg>
<section class="abs services"></section>
<h2 class="abs services-title">Services</h2>
<div class="abs service" style="left:106px;top:1115px"><h3>Internal Pivot Assessment &amp; Post Exploitation</h3><p>We start as a low privilege user and attempt to move through the network in an attempt to access the data the matters to you. This is a simulation of a rogue trusted insider or a compromised internal host. We determine your risk when the egg shell is cracked. Even a seemingly insignificant compromise can have big consequences, and our goal is to demonstrate this risk.</p></div>
<div class="abs service" style="left:449px;top:1115px"><h3>Red Team Adversary Simulation</h3><p>A goal-based assessment where we attack just like a real world adversary. This includes external attacks and targeted phishing to demonstrate the real risk to your data.</p></div>
<div class="abs service" style="left:790px;top:1115px"><h3>Penetration Testing &amp; Vulnerability Assessments</h3><p>This includes vulnerability scans of the in-scope systems where we manually verify issues and exploit any issues found. We report on the issues that actually have a real risk to your organization.</p></div>
<div class="abs service" style="left:106px;top:1397px"><h3>Advanced Product, Hardware &amp; RF Testing</h3><p>This is a highly customized assessment designed for you and your hardware. Depending on the product we will analyze custom RF protocols, reverse engineer OS and firmware, and analyze and fuzz network protocols. We have tested a range of products from toys to security products.</p></div>
<div class="abs service" style="left:449px;top:1397px"><h3>Web Application Penetration Testing</h3><p>Our team will perform an in-depth analysis of your web application to find vulnerabilities related to programming errors, misconfiguration, and application architectural issues. We will perform automated and manual runtime analysis of your application. We create custom test cases to fuzz your application and find the faults before the bad guys do.</p></div>
<div class="abs service" style="left:790px;top:1397px"><h3>Mobile Application Assessment</h3><p>We look at your mobile application and the associated infrastructure to find configuration weaknesses, server-side issues, insecure authentication and access control, and other issues related to the latest attacks on mobile applications.</p></div>

<h2 class="abs about-title">ABOUT US</h2>
<p class="abs about-sub">We focus on hacking. This is our passion. We find the vulnerabilities before the bad guys do.</p>
<div class="abs video" role="img" aria-label="Video still: close-up of an eye behind dark-rimmed glasses"></div>
<div class="abs play-btn"></div>
<svg class="abs" style="left:587px;top:1975px" width="14" height="18" viewBox="0 0 14 18"><path d="M0 0 L14 9 L0 18 Z" fill="#fff"/></svg>
<div class="abs video-controls"></div>
<svg class="abs" style="left:324px;top:2120px" width="12" height="14" viewBox="0 0 12 14"><path d="M0 0 L12 7 L0 14 Z" fill="#fff"/></svg>
<div class="abs progress"></div>
<span class="abs" style="left:354px;top:2122px;width:12px;height:12px;border-radius:50%;background:#fff"></span>
<span class="abs time">0:00 / 0:25</span>
<svg class="abs" style="left:816px;top:2119px" width="16" height="14" viewBox="0 0 16 14"><path d="M0 4 H4 L8 0 V14 L4 10 H0 Z" fill="#fff"/></svg>
<svg class="abs" style="left:844px;top:2120px" width="13" height="13" viewBox="0 0 13 13" fill="none" stroke="#fff" stroke-width="2"><path d="M0 4 V0 H4 M9 0 H13 V4 M13 9 V13 H9 M4 13 H0 V9"/></svg>

<section class="abs testimonial"></section>
<span class="abs quote-mark" style="left:100px">&ldquo;</span>
<span class="abs quote-mark" style="left:872px">&rdquo;</span>
<div class="abs avatar-frame"></div>
<div class="abs avatar" role="img" aria-label="Cartoon avatar of a reviewer on a green circle"></div>
<p class="abs client-name">D.H. (Undisclosed Organization)</p>
<p class="abs client-quote">I read the report yesterday. This is one of the best-written,<br>actionable pentest reports I've ever seen.</p>

<footer class="abs footer"></footer>
<p class="abs footer-heading" style="left:106px;top:2866px">Contact Us</p>
<div class="abs footer-brand"><span class="brand-square"></span><span class="brand-name">Tallow Marsh</span></div>
<p class="abs footer-heading" style="left:790px;top:2866px">QUICK LINKS</p>
<ul class="abs quick-links">
  <li>Home</li><li>What We Do</li><li>Services</li><li>About</li><li>Press</li><li>Blog</li><li>Contact</li>
</ul>
<div class="abs footer-base"></div>
<div class="abs social"><span></span><span></span><span></span><span></span></div>

</body>
</html>
```